Corrabeen Holiday Village Flyer Project

Flyer required for a holiday caravan park. I have attached the current flyer for the park and would like to use the same layout. Please also alter the changes to the text that I have marked up. Until the additional uploads for the new images are ready, could you please just leave those as a blank square and the images can be inserted once I have them loaded.

Target Market(s)

Holiday makers

Industry/Entity Type

Tourism

Colors
3176b5
33a6d7
0393ce
fbee3e
fbed22
ffffff
faa54b

Requirements
Must have
• copy the attached flyer
• Would like a better title font for the front text - "Corrabeen Holiday Village", please make that a more playful holiday feel font
• Please use images 001 & 002 as the front cover images
• I have more images to load up which will be done 4/7.
Nice to have
• would like a better colour back ground to the flyer, maybe blue-ish and then alter the colour of the text accordingly
Should not have
• Please use the attached flyer copy as a template

```html
<!DOCTYPE html>
<html lang="en">
<head>
<meta charset="utf-8">
<title>Corrabeen Holiday Village – Brochure Inside Spread</title>
<link href="https://fonts.googleapis.com/css2?family=Montserrat:wght@400;500;600;700&family=Dancing+Script:wght@700&display=swap" rel="stylesheet">
<style>
  :root {
    --navy-blue: #3176b5;
    --sky-blue: #33a6d7;
    --ocean-blue: #0393ce;
    --sun-yellow: #fbee3e;
    --lime-yellow: #d8d42a;
    --paper: #ffffff;
    --ink: #4a4a4a;
    --ink-dark: #333333;
  }
  * { margin: 0; padding: 0; box-sizing: border-box; }
  html, body { width: 1200px; height: 816px; overflow: hidden; background: #f3f3f3; }
  body { font-family: "Montserrat", Arial, sans-serif; color: var(--ink); }

  .spread { position: relative; width: 1200px; height: 816px; overflow: hidden; }
  .spread-art { position: absolute; inset: 0; }

  .copy { position: absolute; }
  .heading { color: var(--navy-blue); font-weight: 700; line-height: 1; }
  .subheading { color: var(--ocean-blue); font-weight: 700; font-size: 14px; margin-bottom: 8px; }

  .square-list { list-style: none; columns: 2; column-gap: 22px; font-size: 13px; line-height: 15px; }
  .square-list li { position: relative; padding-left: 18px; break-inside: avoid; }
  .square-list li::before {
    content: ""; position: absolute; left: 0; top: 4px; width: 7px; height: 7px;
    background: linear-gradient(var(--sky-blue) 50%, var(--lime-yellow) 50%);
  }
  .square-list.single { columns: 1; }

  /* Panel 1 */
  .what-to-do { left: 42px; top: 38px; width: 330px; }
  .what-to-do .heading { font-size: 34px; margin-bottom: 14px; }
  .activity-group { margin-bottom: 20px; }
  .tagline {
    left: 48px; top: 372px; width: 300px;
    font-family: "Dancing Script", cursive; font-weight: 700; font-size: 32px; line-height: 34px;
    color: var(--ocean-blue);
  }

  /* Panel 2 */
  .accommodation { left: 440px; top: 246px; width: 340px; }
  .accommodation .heading { font-size: 31px; letter-spacing: 0.5px; margin-bottom: 12px; }
  .accommodation .square-list { font-size: 14px; line-height: 19px; }

  /* Panel 3 */
  .facilities { left: 830px; top: 40px; width: 340px; }
  .facilities .heading { font-size: 30px; margin-bottom: 14px; }
  .arrow-list { list-style: none; columns: 2; column-gap: 16px; font-size: 13.5px; line-height: 20px; }
  .arrow-list li { position: relative; padding-left: 18px; }
  .arrow-list li::before {
    content: ""; position: absolute; left: 0; top: 5px; width: 9px; height: 10px;
    background: var(--ocean-blue); clip-path: polygon(0 0, 100% 50%, 0 100%, 30% 50%);
  }
  .nearby { left: 830px; top: 222px; width: 340px; text-align: center; font-weight: 700; font-size: 13px; line-height: 16px; color: var(--ink-dark); }
  .contact { left: 812px; top: 300px; width: 376px; text-align: center; font-size: 10.5px; line-height: 16px; }
  .contact-lead { color: var(--ocean-blue); font-weight: 500; white-space: nowrap; }
  .contact-line { color: var(--ink); font-size: 10px; display: flex; align-items: center; justify-content: center; gap: 6px; }
  .contact-line svg { width: 10px; height: 10px; fill: var(--sky-blue); }
</style>
</head>
<body>
<main class="spread">
  <svg class="spread-art" width="1200" height="816" viewBox="0 0 1200 816">
    <defs>
      <linearGradient id="panel-left" x1="0" x2="1"><stop offset="0" stop-color="#ffffff"/><stop offset="1" stop-color="#f1f1f1"/></linearGradient>
      <linearGradient id="panel-mid" x1="0" x2="1"><stop offset="0" stop-color="#e9e9e9"/><stop offset="0.25" stop-color="#f6f6f6"/><stop offset="1" stop-color="#f2f2f2"/></linearGradient>
      <linearGradient id="panel-right" x1="0" x2="1"><stop offset="0" stop-color="#e6e6e6"/><stop offset="0.2" stop-color="#f4f4f4"/><stop offset="1" stop-color="#fafafa"/></linearGradient>
      <linearGradient id="sunset-tones" x1="0" y1="0" x2="0" y2="1"><stop offset="0" stop-color="#d98a4a"/><stop offset="0.35" stop-color="#7a4a3a"/><stop offset="1" stop-color="#1d2a3c"/></linearGradient>
      <linearGradient id="jetty-tones" x1="0" y1="0" x2="0" y2="1"><stop offset="0" stop-color="#9cc4e4"/><stop offset="0.45" stop-color="#8b8f86"/><stop offset="1" stop-color="#4a4a3e"/></linearGradient>
      <linearGradient id="dolphin-tones" x1="0" y1="0" x2="0" y2="1"><stop offset="0" stop-color="#6c9a6a"/><stop offset="0.25" stop-color="#3aa0b8"/><stop offset="1" stop-color="#0b6c86"/></linearGradient>
      <linearGradient id="aerial-tones" x1="0" y1="0" x2="1" y2="1"><stop offset="0" stop-color="#2b8fb0"/><stop offset="0.5" stop-color="#8a7a64"/><stop offset="1" stop-color="#1f7fa0"/></linearGradient>
      <clipPath id="panel-one"><rect x="0" y="0" width="400" height="816"/></clipPath>
      <clipPath id="panel-two"><rect x="400" y="0" width="400" height="816"/></clipPath>
      <clipPath id="panel-three"><rect x="800" y="0" width="400" height="816"/></clipPath>
    </defs>

    <rect class="panel" x="0" y="0" width="400" height="816" fill="url(#panel-left)"/>
    <rect class="panel" x="400" y="0" width="400" height="816" fill="url(#panel-mid)"/>
    <rect class="panel" x="800" y="0" width="400" height="816" fill="url(#panel-right)"/>

    <g clip-path="url(#panel-two)">
      <ellipse cx="610" cy="60" rx="200" ry="158" fill="var(--lime-yellow)"/>
      <ellipse cx="610" cy="52" rx="188" ry="146" fill="var(--ocean-blue)"/>
      <ellipse role="img" aria-label="Photo: sunset over the ocean" cx="612" cy="40" rx="170" ry="128" fill="url(#sunset-tones)"/>
    </g>

    <path d="M290 816 L290 640 Q360 560 470 590 Q560 540 660 545 Q770 520 900 545 L920 816 Z" fill="var(--navy-blue)"/>
    <path d="M310 816 L310 650 Q380 585 480 605 Q570 560 660 562 Q770 540 890 560 L900 816 Z" fill="var(--lime-yellow)"/>
    <path role="img" aria-label="Photo: dolphin leaping from the water" d="M330 816 L330 660 Q400 605 490 620 Q580 580 660 580 Q770 560 880 578 L880 816 Z" fill="url(#dolphin-tones)"/>

    <g clip-path="url(#panel-three)">
      <circle cx="1080" cy="665" r="268" fill="var(--ocean-blue)"/>
      <circle cx="1095" cy="667" r="252" fill="var(--lime-yellow)"/>
      <circle cx="1108" cy="670" r="238" fill="var(--sky-blue)"/>
      <circle role="img" aria-label="Photo: aerial view of the estuary, canals and bridge" cx="1122" cy="673" r="222" fill="url(#aerial-tones)"/>
    </g>

    <g clip-path="url(#panel-one)">
      <circle cx="175" cy="850" r="300" fill="var(--lime-yellow)"/>
      <circle cx="175" cy="852" r="286" fill="var(--ocean-blue)"/>
      <circle role="img" aria-label="Photo: family crabbing from a wooden jetty" cx="170" cy="860" r="268" fill="url(#jetty-tones)"/>
    </g>

    <rect x="396" y="0" width="8" height="816" fill="#000" opacity="0.04"/>
    <rect x="796" y="0" width="8" height="816" fill="#000" opacity="0.05"/>
  </svg>

  <section class="copy what-to-do">
    <h2 class="heading">What to do ?</h2>
    <div class="activity-group">
      <p class="subheading">The Estuary is only 2mins to the east for....</p>
      <ul class="square-list">
        <li>Water sports</li><li>Crabbing</li><li>Boating</li>
        <li>Swimming</li><li>Prawning</li><li>Boat Ramp Access</li>
      </ul>
    </div>
    <div class="activity-group">
      <p class="subheading">Melrose Beach is 56mins to the west for....</p>
      <ul class="square-list">
        <li>Water Skiing</li><li>Swimming</li><li>Crabbing</li><li>Boat Ramp Access</li>
        <li>Sailing</li><li>Fishing</li><li>Surfing</li><li>Beach Walking</li>
      </ul>
    </div>
    <div class="activity-group">
      <p class="subheading">Sporting Facilities 5mins</p>
      <ul class="square-list">
        <li>Golfing</li><li>Bowls</li>
      </ul>
    </div>
  </section>
  <p class="copy tagline">The best crabbing in Mandurah</p>

  <section class="copy accommodation">
    <h2 class="heading">ACCOMMODATION</h2>
    <ul class="square-list single">
      <li>Chalets Ensuite &amp; Air Con</li>
      <li>Caravans</li>
      <li>Caravans &amp; Air Con</li>
      <li>Caravans Ensuite &amp; Air Con</li>
      <li>Powered Sites</li>
    </ul>
  </section>

  <section class="copy facilities">
    <h2 class="heading">FACILITIES</h2>
    <ul class="arrow-list">
      <li>EFTPOS</li><li>Swimming Pool</li><li>Undercover BBQ</li><li>Crab Cooker</li>
      <li>Playground</li><li>Laundrette</li><li>TV Room</li><li>Games Room</li>
    </ul>
  </section>
  <p class="copy nearby">2 Supermarkets within 2 mins<br>13 Take-away shops within 7 mins<br>6 Restaurants within 7 mins<br>Mandurah CBD 15 mins</p>
  <div class="copy contact">
    <p class="contact-lead">For more information please contact us or visit our website</p>
    <p class="contact-line"><svg viewBox="0 0 10 10"><circle cx="5" cy="5" r="4.5"/></svg>www.corrabeenvillage.com.au</p>
    <p class="contact-line"><svg viewBox="0 0 10 10"><path d="M2 0.5 L4 2.5 L3 4 Q4.5 6 6 7 L7.5 6 L9.5 8 L8 9.5 Q3 9 0.5 2 Z"/></svg>(08) 5550 1234</p>
  </div>
</main>
</body>
</html>
```